Business Card Design

Please visit www.RobHartwell.com to acquire information for business card.

Back Side of Card:
a lifetime of experience working for you.

With over 25 years in the construction industry, well over a decade as a licensed Subcontractor / General Contractor and nearly 10 years as a licensed Realtor, I have excelled and cultivated a working knowledge of how all the pieces fit together.

Here is a link to folder.
https://files.examplestore.net/folderview?id=7Kq2XwPmR4tLvN9sBz8yHc3DfGaJ&usp=sharing

Industry/Entity Type

Construction

Contact Information for Business Card

Company: Rob Hartwell, LLC.
Address: 31872 W. Cedar Hollow Blvd. Suite 207-384
Name: Rob Hartwell
Phone: (623) 587-2914
Web: www.RobHartwell.com
Type of services offered: Architectural Design, 3D Models, Renderings & Animation - Construction Documents - Project Managment.

```html
<!DOCTYPE html>
<html lang="en">
<head>
<meta charset="utf-8">
<title>Rob Hartwell, LLC. – Business Card</title>
<link rel="stylesheet" href="https://fonts.googleapis.com/css2?family=Arimo:wght@400;700&family=Tinos:wght@700&display=swap">
<style>
  :root {
    --bg: #eec3c9;
    --teal: #12a9b5;
    --teal-deep: #0c9aa6;
    --grey: #8f8f8f;
    --grey-deep: #7a7a7a;
    --white: #ffffff;
    --card-w: 500px;
    --card-h: 286px;
  }
  * { margin: 0; padding: 0; box-sizing: border-box; }
  html, body { width: 1200px; height: 675px; overflow: hidden; }
  body {
    background: var(--bg);
    font-family: "Arimo", Arial, sans-serif;
    color: var(--white);
    display: flex;
    align-items: center;
    justify-content: center;
    gap: 60px;
  }
  .card {
    position: relative;
    width: var(--card-w);
    height: var(--card-h);
    overflow: hidden;
    box-shadow: 0 6px 18px rgba(90, 30, 40, 0.25);
  }

  /* ---------- Back side ---------- */
  .card-back { background: linear-gradient(135deg, #9a9a9a, var(--grey-deep)); }
  .card-back .teal-block {
    position: absolute; left: 0; top: 0; bottom: 0; width: 45%;
    background: linear-gradient(160deg, var(--teal), var(--teal-deep));
  }
  .card-back .rule {
    position: absolute; left: 0; right: 0; height: 3px; background: var(--white);
  }
  .card-back .rule-top { top: 8%; }
  .card-back .rule-bottom { top: 82%; }
  .card-back .wordmark {
    position: absolute; left: 45%; top: 44%;
    transform: translate(-50%, -50%);
    font-size: 16px; font-weight: 400; white-space: nowrap;
    color: var(--white);
  }

  /* ---------- Front side ---------- */
  .card-front { background: linear-gradient(150deg, #1bbcc6, var(--teal-deep)); }
  .card-front .divider {
    position: absolute; left: 56%; top: 0; bottom: 0; width: 3px; background: var(--white);
  }
  .card-front .services-panel {
    position: absolute; left: calc(56% + 3px); right: 0; top: 48%; bottom: 0;
    background: linear-gradient(135deg, #939393, var(--grey-deep));
  }
  .card-front .name-plate {
    position: absolute; left: 23%; top: 40%; width: 33%; height: 38px;
    background: var(--grey);
    display: flex; align-items: center; justify-content: center;
    font-family: "Tinos", "Times New Roman", serif; font-weight: 700;
    font-size: 17px; white-space: nowrap; color: var(--white);
  }
  .card-front .contact {
    position: absolute; left: calc(56% + 16px); right: 14px; top: 14%;
    font-size: 12px; line-height: 1.4; text-align: right;
  }
  .card-front .contact b { font-weight: 700; }
  .card-front .services {
    position: absolute; left: calc(56% + 14px); right: 12px; top: 56%;
    font-size: 11.5px; line-height: 1.35; text-align: center;
  }
  .card-front .services b { font-size: 14px; font-weight: 700; }
</style>
</head>
<body>
  <section class="card card-back" aria-label="Card back">
    <div class="teal-block"></div>
    <div class="rule rule-top"></div>
    <div class="rule rule-bottom"></div>
    <p class="wordmark">Rob Hartwell LLC</p>
  </section>

  <section class="card card-front" aria-label="Card front">
    <div class="services-panel"></div>
    <div class="divider"></div>
    <p class="name-plate">Rob Hartwell LLC</p>
    <div class="contact">
      <p><b>Name:</b>Rob Hartwell</p>
      <p><b>Ph:</b>(623) 587-2914</p>
      <p><b>Address:</b> 31872 W. Cedar Hollow Blvd. Suite 207-384</p>
      <p><b>Url:</b>www.RobHartwell.com</p>
    </div>
    <p class="services"><b>services:</b> Architectural Design, 3D Models, Renderings &amp; Animation - Construction Documents - Project Managment.</p>
  </section>
</body>
</html>
```